Willowmere Acres Brand - Bag Design

We are a company dealing with nuts, grains and seeds and are looking for a design for our retail bag packaging that will be consistent across all our product range. We are currently differentiating in way of color but please feel free to be more creative if you wish. Sample of products include pumpkin seeds, rolled oats, almonds, etc.
Design Idea: Hygienic, Natural (from Nature), Quality & Upscale, Simple & Clean design
Target Market: High-end Markets, end-users of A/B type.
1. Bag size is 210 mm (width) * 310 mm (length). Material is OPP or multi-layer PP.
2. Front must have clear window to show packed products. Back clear window is optional.
3. Front side must have logo that stands out (Willowmere Acres) as attached.
4. Front side must have product name and net weight.
5. Back side must have enough space for Nutrition Fact, product descriptions (110 mm * 100 mm), and barcode.
6. Back side must have white space to print production and expiry dates about 25 mm * 30 mm.
7. Top and bottom of bag must be opaque and not show product.
Updates
Project Deadline Extended
Reason: Extended period for more new ideas and also for requested modification.
Target Market(s)
Premium market. Type A to B customers as well as professional clients. The product is not a snack. It is for cooking or baking.
Industry/Entity Type
Food Store
Requirements
Must have
- Look unique and stand out from others in the market.
- The colors of the word "Willowmere Acres" and the blue air-brush in the logo can be changed.
Nice to have
- See project description
Should not have
- See project description

```html
<!DOCTYPE html>
<html lang="en">
<head>
<meta charset="utf-8">
<title>Willowmere Acres – Bag Range</title>
<link rel="stylesheet" href="https://fonts.googleapis.com/css2?family=Arvo:wght@400;700&display=swap">
<style>
  :root {
    --stage: #756c63;
    --label: #f3f2ef;
    --dots: #3a3a3a;
    --almond-bag: #b8442e;
    --almond-ink: #ad1f2c;
    --oats-bag: #7e6656;
    --oats-ink: #7a6254;
    --pumpkin-bag: #b9af88;
    --pumpkin-ink: #1f8a3a;
    --brand-ink: #7a8a1c;
    --almond-fill: #a8713e;
    --oats-fill: #d9cfaa;
    --pumpkin-fill: #7f875a;
  }
  * { margin: 0; padding: 0; box-sizing: border-box; }
  html, body { width: 1200px; height: 900px; overflow: hidden; }
  body {
    background: var(--stage);
    font-family: "Arvo", serif;
    position: relative;
  }
  .bag {
    position: absolute;
    top: 255px;
    width: 302px;
    height: 444px;
    border-radius: 4px;
    overflow: hidden;
  }
  .bag--almonds { left: 124px; }
  .bag--oats { left: 458px; }
  .bag--pumpkin { left: 793px; }

  .bag__pattern { position: absolute; inset: 0; }
  .bag--almonds .bag__pattern { background: var(--almond-bag); }
  .bag--oats .bag__pattern { background: var(--oats-bag); }
  .bag--pumpkin .bag__pattern { background: var(--pumpkin-bag); }

  .label {
    position: absolute;
    left: 65px;
    top: 74px;
    width: 172px;
    bottom: 0;
    background: var(--label);
    text-align: center;
  }
  .label__top {
    position: absolute;
    inset: 5px 5px auto 5px;
    height: 166px;
    border: 1px dotted var(--dots);
    border-bottom: none;
  }
  .label__bottom {
    position: absolute;
    inset: auto 5px 5px 5px;
    height: 89px;
    border: 1px dotted var(--dots);
    border-top: none;
  }
  .brand {
    position: absolute;
    top: 55px;
    left: 0; right: 0;
    display: flex;
    justify-content: center;
    align-items: center;
    gap: 5px;
    font-size: 12px;
    font-weight: 400;
    color: var(--brand-ink);
  }
  .brand__dot {
    width: 10px; height: 10px;
    border-radius: 50%;
    background: var(--brand-ink);
  }
  .product-name {
    position: absolute;
    top: 92px;
    left: 0; right: 0;
    font-weight: 700;
    line-height: 28px;
  }
  .product-name__main { display: block; font-size: 25px; letter-spacing: 0.5px; }
  .product-name__sub { display: block; font-size: 23px; letter-spacing: 1px; }
  .bag--almonds .product-name, .bag--almonds .claim { color: var(--almond-ink); }
  .bag--oats .product-name, .bag--oats .claim { color: var(--oats-ink); }
  .bag--pumpkin .product-name, .bag--pumpkin .claim { color: var(--pumpkin-ink); }

  .window {
    position: absolute;
    left: 53px;
    top: 246px;
    width: 196px;
    height: 110px;
    border-radius: 50%;
    border: 5px solid #e6e5e2;
    box-shadow: 0 0 0 1px rgba(0,0,0,0.25);
  }
  .bag--almonds .window { background: radial-gradient(ellipse at center, #c28a52, var(--almond-fill)); }
  .bag--oats .window { background: radial-gradient(ellipse at center, #ece4c4, var(--oats-fill)); }
  .bag--pumpkin .window { background: radial-gradient(ellipse at center, #9aa06e, var(--pumpkin-fill)); }

  .claim {
    position: absolute;
    top: 304px;
    left: 0; right: 0;
    font-size: 13px;
    font-weight: 700;
    letter-spacing: 0.5px;
  }
  .net-weight {
    position: absolute;
    top: 347px;
    left: 0; right: 0;
    font-size: 8px;
    font-weight: 700;
    color: #9b1b24;
  }
  .bag--oats .net-weight { color: #6b564a; }
  .bag--pumpkin .net-weight { color: #1c6e31; }
</style>
</head>
<body>

  <section class="bag bag--almonds">
    <div class="bag__pattern" role="img" aria-label="Red bag face with white diagonal chevron stripes"></div>
    <div class="label">
      <div class="label__top"></div>
      <div class="label__bottom"></div>
      <div class="brand"><span class="brand__dot"></span>Willowmere Acres</div>
      <h2 class="product-name"><span class="product-name__main">ALMONDS</span><span class="product-name__sub">• SEEDS •</span></h2>
      <p class="claim">ORGANIC PRODUCT</p>
      <p class="net-weight">NET WT 11 OZ ( 312 G )</p>
    </div>
    <div class="window" role="img" aria-label="Clear window showing whole almonds"></div>
  </section>

  <section class="bag bag--oats">
    <div class="bag__pattern" role="img" aria-label="Brown bag face with white diagonal chevron stripes"></div>
    <div class="label">
      <div class="label__top"></div>
      <div class="label__bottom"></div>
      <div class="brand"><span class="brand__dot"></span>Willowmere Acres</div>
      <h2 class="product-name"><span class="product-name__main">ROLLED</span><span class="product-name__sub">• OATS •</span></h2>
      <p class="claim">ORGANIC PRODUCT</p>
      <p class="net-weight">NET WT 11 OZ ( 312 G )</p>
    </div>
    <div class="window" role="img" aria-label="Clear window showing rolled oat flakes"></div>
  </section>

  <section class="bag bag--pumpkin">
    <div class="bag__pattern" role="img" aria-label="Khaki bag face with white diagonal chevron stripes"></div>
    <div class="label">
      <div class="label__top"></div>
      <div class="label__bottom"></div>
      <div class="brand"><span class="brand__dot"></span>Willowmere Acres</div>
      <h2 class="product-name"><span class="product-name__main">PUMPKIN</span><span class="product-name__sub">• SEEDS •</span></h2>
      <p class="claim">ORGANIC PRODUCT</p>
      <p class="net-weight">NET WT 11 OZ ( 312 G )</p>
    </div>
    <div class="window" role="img" aria-label="Clear window showing green pumpkin seeds"></div>
  </section>

</body>
</html>
```